Pine Hill Drafting - Flyer Design

I'm looking for good designs of the 2 sided flyer size DL (210 x 95 mm)
Please make sure the design is in the same colours as my business card. Image attached.
Include Architectural plan at the background.
Please note that some words are in capital letters...
FRONT PAGE including :
Are you planning to RENOVATE, EXTEND the house, build new GRANNY FLAT?
Do you need assistance with DA , COMPLYING DEVELOPMENT?
Is your building budget tight and you DON'T WANT to spend it on the ARCHITECTURAL FEES?
For free obligation quote contact:
PINE HILL DRAFTING
pinehilldrafting@mailnest.net.au
Dorte - 0482 657 930
For more details check: www.pinehilldrafting.net.au
Follow us on chatterly: www.chatterly.net/pinehilldrafting
BACK PAGE including:
Services
- Building Design
- Architectural Drafting
- 3D Modelling
- Norvo Assessment
- Building Specifications
- Council Submission Services
- Coordination with Building Professionals
Contact Dorte on 0482 657 930 or pinehilldrafting@mailnest.net.au for obligation free quote

```html
<!DOCTYPE html>
<html lang="en">
<head>
<meta charset="utf-8">
<title>Pine Hill Drafting – DL Flyer</title>
<link rel="stylesheet" href="https://fonts.googleapis.com/css2?family=Arimo:wght@400;700&display=swap">
<style>
  :root {
    --stage: #3b3b3e;
    --brand-blue: #1ea3d8;
    --brand-blue-deep: #1590c4;
    --white: #ffffff;
    --plan-light: #eef2f4;
    --plan-mid: #cfd8de;
    --screen-blue: #9fc7d9;
  }
  * { box-sizing: border-box; margin: 0; padding: 0; }
  html, body { width: 1200px; height: 1154px; overflow: hidden; }
  body {
    background: var(--stage);
    font-family: "Arimo", Arial, sans-serif;
    color: var(--white);
    position: relative;
  }
  .flyer {
    position: absolute;
    top: 80px;
    width: 460px;
    height: 1018px;
    background: var(--brand-blue);
    overflow: hidden;
  }
  .flyer--front { left: 111px; }
  .flyer--back { left: 628px; }
  .flyer > * { position: absolute; left: 0; right: 0; }

  /* Front */
  .front-headline {
    top: 34px;
    text-align: center;
    font-size: 17px;
    line-height: 24px;
  }
  .hero-visual {
    top: 96px;
    height: 409px;
    background: radial-gradient(ellipse at 45% 45%, var(--screen-blue) 0%, var(--plan-mid) 45%, var(--plan-light) 100%);
  }
  .front-questions {
    top: 519px;
    text-align: center;
    font-size: 17px;
    line-height: 24px;
  }
  .front-questions p + p { margin-top: 10px; }
  .quote-lead {
    top: 696px;
    left: 65px;
    font-size: 14px;
  }
  .rule {
    height: 1px;
    background: var(--white);
    opacity: 0.85;
  }
  .front-rule-top { top: 719px; left: 22px; right: 45px; }
  .front-rule-bottom { top: 833px; left: 22px; right: 45px; }
  .brand-name {
    top: 752px;
    left: 22px; right: 45px;
    text-align: center;
    font-size: 44px;
    font-weight: 700;
    line-height: 52px;
  }
  .front-contact {
    top: 848px;
    text-align: center;
  }
  .contact-email { font-size: 16px; line-height: 22px; }
  .contact-phone { font-size: 19px; font-weight: 700; line-height: 24px; }
  .small-label { font-size: 13px; line-height: 17px; }
  .link-line { font-size: 16px; line-height: 19px; }
  .front-contact .small-label:first-of-type { margin-top: 6px; }
  .front-contact .gap { margin-top: 6px; }

  /* Back */
  .services-band {
    top: 34px;
    height: 48px;
    background: var(--white);
  }
  .services-title {
    position: absolute;
    left: 51px;
    top: 10px;
    font-size: 25px;
    letter-spacing: 2px;
    color: var(--brand-blue);
  }
  .service-list {
    top: 102px;
    left: 51px;
    list-style: none;
    font-size: 17px;
    line-height: 29px;
  }
  .back-links {
    top: 350px;
    text-align: center;
  }
  .back-links .gap { margin-top: 4px; }
  .back-rule { top: 454px; left: 51px; right: 44px; }
  .back-contact {
    top: 474px;
    text-align: center;
    font-size: 17px;
    line-height: 30px;
  }
  .back-contact strong { font-weight: 700; }
  .plans-visual {
    top: 582px;
    bottom: 0;
    background: linear-gradient(160deg, var(--plan-light) 0%, var(--white) 45%, var(--plan-mid) 100%);
  }
</style>
</head>
<body>

<section class="flyer flyer--front">
  <p class="front-headline">Are you planning to RENOVATE, EXTEND<br>the house, build new GRANNY FLAT?</p>
  <div class="hero-visual" role="img" aria-label="Hand touching a tablet showing a floor plan, resting on architectural drawings"></div>
  <div class="front-questions">
    <p>Do you need assistance with DA ,<br>COMPLYING DEVELOPMENT?</p>
    <p>Is your building budget tight and you<br>DON'T WANT to spend it on the<br>ARCHITECTURAL FEES?</p>
  </div>
  <p class="quote-lead">For free obligation quote contact:</p>
  <div class="rule front-rule-top"></div>
  <p class="brand-name">Pine Hill Drafting</p>
  <div class="rule front-rule-bottom"></div>
  <div class="front-contact">
    <p class="contact-email">pinehilldrafting@mailnest.net.au</p>
    <p class="contact-phone">Dorte - 0482 657 930</p>
    <p class="small-label">For more details check:</p>
    <p class="link-line">www.pinehilldrafting.net.au</p>
    <p class="small-label gap">Follow us on chatterly:</p>
    <p class="link-line">www.chatterly.net/pinehilldrafting</p>
  </div>
</section>

<section class="flyer flyer--back">
  <div class="services-band"><h2 class="services-title">SERVICES</h2></div>
  <ul class="service-list">
    <li>- Building Design</li>
    <li>- Architectural Drafting</li>
    <li>- 3D Modelling</li>
    <li>- Norvo Assessment</li>
    <li>- Building Specifications</li>
    <li>- Council Submission Services</li>
    <li>- Coordination with Building Professionals</li>
  </ul>
  <div class="back-links">
    <p class="small-label">For more details check:</p>
    <p class="link-line">www.pinehilldrafting.net.au</p>
    <p class="small-label gap">Follow us on chatterly:</p>
    <p class="link-line">www.chatterly.net/pinehilldrafting</p>
  </div>
  <div class="rule back-rule"></div>
  <p class="back-contact">Contact Dorte on <strong>0482 657 930</strong> or<br><strong>pinehilldrafting@mailnest.net.au</strong> for<br>obligation free quote</p>
  <div class="plans-visual" role="img" aria-label="Rolled architectural floor plan drawings"></div>
</section>

</body>
</html>
```